Brelora
business card, seafood selling company
Professional
Kaloyan Terziev
Manager
14A, Vasil Mirkov str,
Sofia, Bulgaria,
postal code: 1486
k.terziev@brelora-demo.bg
www.brelora-demo.bg
I want a good looking and stylish business card.
I didn't decide it yet. I hope I will receive good and fresh ideas.
Here is our logo which have to be used in the business card

```html
<!DOCTYPE html>
<html lang="en">
<head>
<meta charset="utf-8">
<title>Brelora – stationery set</title>
<link href="https://fonts.googleapis.com/css2?family=Montserrat:wght@400;600;800&display=swap" rel="stylesheet">
<style>
  :root{
    --navy:#1d3a8c;
    --navy-dark:#142a6b;
    --orange:#f05a28;
    --paper:#ffffff;
    --ink:#4a4a4a;
    --backdrop:#e7e4e0;
  }
  *{box-sizing:border-box;margin:0;padding:0}
  html,body{width:1200px;height:638px;overflow:hidden}
  body{background:var(--backdrop);font-family:"Montserrat",Arial,sans-serif;color:var(--ink);position:relative}
  .piece{position:absolute;overflow:hidden;background:var(--paper);box-shadow:0 2px 6px rgba(0,0,0,.18)}
  .piece svg.wave{position:absolute;left:0;width:100%}
  .brand{display:flex;align-items:center;gap:5px;font-weight:800;color:var(--navy);letter-spacing:.5px;position:absolute}
  .brand .dot{width:10px;height:10px;border-radius:50%;background:var(--orange)}
  .brand.light{color:#fff}
  .brand.light .dot{background:#fff}
  .tagline{position:absolute;font-size:5px;letter-spacing:.4px;color:var(--orange)}
  .contact{position:absolute;font-size:5.5px;line-height:1.5;color:var(--ink)}
  .person{position:absolute;font-size:6px;line-height:1.4;text-align:right}
  .person b{font-weight:600;color:var(--navy)}

  /* business cards */
  .card{width:212px;height:136px;border-radius:6px}
  .card-front{left:86px;top:72px}
  .card-orange{left:316px;top:72px;background:var(--orange)}
  .card-navy{left:86px;top:218px;background:var(--navy)}
  .card-back{left:316px;top:218px}

  /* letterheads */
  .letterhead{width:266px;height:432px;top:72px}
  .letterhead-a{left:557px}
  .letterhead-b{left:848px}

  /* envelopes */
  .envelope{width:250px;height:118px}
  .envelope-orange{left:86px;top:362px}
  .envelope-navy{left:214px;top:410px}
  .envelope-white{left:336px;top:466px;height:110px;width:228px}
  .dl{width:258px;height:96px;top:516px}
  .dl-a{left:570px}
  .dl-b{left:848px}
  .flap{position:absolute;left:0;top:0;width:100%}
</style>
</head>
<body>

<!-- card: front -->
<div class="piece card card-front">
  <div class="brand" style="left:14px;top:14px;font-size:15px"><span class="dot"></span>Brelora</div>
  <div class="tagline" style="left:31px;top:33px">FISH &amp; SEAFOOD TRADING</div>
  <div class="person" style="right:14px;top:16px"><b>Kaloyan Terziev</b><br>Manager</div>
  <div class="contact" style="left:14px;top:54px">
    14A, Vasil Mirkov str,<br>Sofia, Bulgaria, 1486<br>+359 2 400 1486<br>k.terziev@brelora-demo.bg<br>www.brelora-demo.bg
  </div>
  <svg class="wave" style="bottom:0" height="40" viewBox="0 0 212 40" preserveAspectRatio="none">
    <path d="M0 22 C60 2 130 36 212 8 L212 40 L0 40Z" fill="var(--orange)"/>
    <path d="M0 28 C60 10 130 42 212 16 L212 40 L0 40Z" fill="var(--navy)"/>
  </svg>
</div>

<!-- card: orange -->
<div class="piece card card-orange">
  <div class="brand light" style="left:30px;top:30px;font-size:20px"><span class="dot"></span>Brelora</div>
  <svg class="wave" style="bottom:0" height="44" viewBox="0 0 212 44" preserveAspectRatio="none">
    <path d="M0 24 C70 4 140 40 212 12 L212 44 L0 44Z" fill="#fff"/>
  </svg>
</div>

<!-- card: navy -->
<div class="piece card card-navy">
  <div class="brand light" style="left:14px;top:18px;font-size:16px"><span class="dot"></span>Brelora</div>
  <div class="tagline" style="left:31px;top:39px;color:#fff">FISH &amp; SEAFOOD TRADING</div>
  <svg class="wave" style="bottom:0" height="46" viewBox="0 0 212 46" preserveAspectRatio="none">
    <path d="M0 30 C70 8 140 44 212 14 L212 46 L0 46Z" fill="var(--navy-dark)"/>
    <path d="M0 34 C70 14 140 48 212 20" stroke="var(--orange)" stroke-width="2" fill="none"/>
  </svg>
</div>

<!-- card: white back -->
<div class="piece card card-back">
  <svg class="wave" style="top:0" height="136" viewBox="0 0 212 136" preserveAspectRatio="none">
    <path d="M0 0 L212 0 L212 30 C140 10 70 50 0 24Z" fill="var(--navy)"/>
    <path d="M0 24 C70 50 140 10 212 30" stroke="var(--orange)" stroke-width="3" fill="none"/>
    <path d="M0 112 C70 92 140 128 212 100 L212 136 L0 136Z" fill="var(--navy)"/>
  </svg>
  <div class="brand" style="left:44px;top:52px;font-size:20px"><span class="dot"></span>Brelora</div>
  <div class="tagline" style="left:65px;top:76px">FISH &amp; SEAFOOD TRADING</div>
</div>

<!-- letterhead A -->
<div class="piece letterhead letterhead-a">
  <svg class="wave" style="top:0" height="40" viewBox="0 0 266 40" preserveAspectRatio="none">
    <path d="M0 0 L266 0 L266 10 C180 30 80 4 0 20Z" fill="var(--navy)"/>
    <path d="M0 22 C80 6 180 32 266 12" stroke="var(--orange)" stroke-width="3" fill="none"/>
  </svg>
  <div class="brand" style="left:84px;top:34px;font-size:15px"><span class="dot"></span>Brelora</div>
  <div class="contact" style="left:186px;top:58px;font-size:5px">14A, Vasil Mirkov str,<br>Sofia, Bulgaria, 1486<br>+359 2 400 1486<br>www.brelora-demo.bg</div>
  <svg class="wave" style="bottom:0" height="90" viewBox="0 0 266 90" preserveAspectRatio="none">
    <path d="M0 30 C90 80 170 0 266 36 L266 90 L0 90Z" fill="var(--orange)"/>
    <path d="M0 40 C90 90 170 10 266 46 L266 90 L0 90Z" fill="var(--navy)"/>
  </svg>
</div>

<!-- letterhead B -->
<div class="piece letterhead letterhead-b">
  <svg class="wave" style="top:0" height="40" viewBox="0 0 266 40" preserveAspectRatio="none">
    <path d="M0 0 L266 0 L266 10 C180 30 80 4 0 20Z" fill="var(--navy)"/>
    <path d="M0 22 C80 6 180 32 266 12" stroke="var(--orange)" stroke-width="3" fill="none"/>
  </svg>
  <div class="brand" style="left:84px;top:34px;font-size:15px"><span class="dot"></span>Brelora</div>
  <div class="contact" style="left:186px;top:58px;font-size:5px">14A, Vasil Mirkov str,<br>Sofia, Bulgaria, 1486<br>+359 2 400 1486<br>www.brelora-demo.bg</div>
  <div class="contact" style="left:20px;top:298px;font-size:5px">Kaloyan Terziev<br>14A, Vasil Mirkov str,<br>Sofia, Bulgaria, 1486<br>k.terziev@brelora-demo.bg</div>
  <svg class="wave" style="bottom:0" height="90" viewBox="0 0 266 90" preserveAspectRatio="none">
    <path d="M0 30 C90 80 170 0 266 36 L266 90 L0 90Z" fill="var(--orange)"/>
    <path d="M0 40 C90 90 170 10 266 46 L266 90 L0 90Z" fill="var(--navy)"/>
  </svg>
</div>

<!-- envelopes -->
<div class="piece envelope envelope-orange">
  <svg class="flap" height="50" viewBox="0 0 250 50" preserveAspectRatio="none">
    <path d="M0 0 L250 0 L250 18 L125 50 L0 18Z" fill="var(--orange)"/>
  </svg>
  <div class="brand light" style="left:113px;top:10px;font-size:0"><span class="dot" style="width:14px;height:14px"></span></div>
</div>

<div class="piece envelope envelope-navy">
  <svg class="flap" height="50" viewBox="0 0 250 50" preserveAspectRatio="none">
    <path d="M0 0 L250 0 L250 18 L125 50 L0 18Z" fill="var(--navy)"/>
    <path d="M0 18 L125 50 L250 18" stroke="var(--orange)" stroke-width="2" fill="none"/>
  </svg>
  <div class="brand light" style="left:113px;top:10px;font-size:0"><span class="dot" style="width:14px;height:14px"></span></div>
</div>

<div class="piece envelope envelope-white">
  <svg class="flap" height="46" viewBox="0 0 228 46" preserveAspectRatio="none">
    <path d="M0 0 L228 0 L228 16 L114 46 L0 16Z" fill="#f4f4f4"/>
    <path d="M0 16 L114 46 L228 16" stroke="#d9d9d9" stroke-width="1" fill="none"/>
  </svg>
  <div class="brand" style="left:84px;top:14px;font-size:11px"><span class="dot"></span>Brelora</div>
</div>

<div class="piece dl dl-a">
  <div class="brand" style="left:12px;top:10px;font-size:11px"><span class="dot"></span>Brelora</div>
  <div class="contact" style="left:12px;top:54px;font-size:4.5px">14A, Vasil Mirkov str,<br>Sofia, Bulgaria, 1486</div>
  <svg class="wave" style="top:0;left:auto;right:0;width:70%" height="96" viewBox="0 0 180 96" preserveAspectRatio="none">
    <path d="M180 0 L180 40 C120 30 60 80 0 96 L180 96Z" fill="var(--navy)"/>
    <path d="M180 36 C120 26 60 76 0 92" stroke="var(--orange)" stroke-width="3" fill="none"/>
  </svg>
</div>

<div class="piece dl dl-b">
  <div class="contact" style="left:14px;top:12px;font-size:4.5px">14A, Vasil Mirkov str,<br>Sofia, Bulgaria, 1486<br>www.brelora-demo.bg</div>
</div>

</body>
</html>
```